Plovanta medical teaching of the future

responsive website, onepager, for medical technology company. It has to look clean and high tech.

Look & feel
• Responsive
• Clean
• Combination icons + foto's
• Integration of a YouTube video

Landingpage items

• Header: picture + 'a video-based teaching platform for surgical procedures'
• About Deferred live medical teaching: Short description
• Features
o Video
o Teaching platform

• Benefits:
o More effective learning
o Faster sharing of knowledge & tecniques
o More cost effective

• References

• Products:
o Live (+link to more info)
o Qorvex (+ link to more info)
o Qorvex local (+link to more info)
o Qorvex cloud (+ link to more info)

• Solutions:
o For medical device companies (+link to more info)
o Doctor and surgeons (+link to more info)
o Medical conferences (+link to more info)

Target Market(s)

medical device companies
surgeons and doctors
conference organisers

Industry/Entity Type

It Company

Number of Pages Required

1 page

Requirements
Must have
• Landingpage items
• • Header: picture + 'a video-based teaching platform for surgical procedures'
• • About Deferred live medical teaching: Short description
• • Features
• o Video
• o Teaching platform
• • Benefits:
• o More effective learning
• o Faster sharing of knowledge & tecniques
• o More cost effective
• • References
• • Products:
• o Live (+link to more info)
• o Qorvex (+ link to more info)
• o Qorvex local (+link to more info)
• o Qorvex cloud (+ link to more info)
• • Solutions:
• o For medical device companies (+link to more info)
• o Doctor and surgeons (+link to more info)
• o Medical conferences (+link to more info)
Nice to have
• possibilty to show video

```html
<!DOCTYPE html>
<html lang="en">
<head>
<meta charset="utf-8">
<title>Plovanta – Deferred Live Medical Teaching</title>
<link rel="stylesheet" href="https://fonts.googleapis.com/css2?family=Glegoo:wght@400;700&family=Open+Sans:wght@400;600&display=swap">
<style>
:root{
  --teal:#27a08f;
  --teal-dark:#1f8a7b;
  --red:#e31e24;
  --ink:#222;
  --body:#555;
  --muted:#777;
  --line:#ddd;
  --grey-bg:#f2f2f2;
  --footer-bg:#f4f4f4;
  --white:#fff;
}
*{box-sizing:border-box;margin:0;padding:0}
html,body{width:1200px;height:3315px;overflow:hidden}
body{font-family:"Open Sans",Arial,sans-serif;color:var(--body);background:var(--white);font-size:15px;line-height:1.6}
a{text-decoration:none;color:inherit}
h2{font-family:"Glegoo",Georgia,serif;font-weight:400;color:var(--ink);font-size:25px;text-align:center}
.lead{text-align:center;font-size:15px;line-height:1.75;color:var(--body)}

/* header */
.site-header{height:84px;display:flex;align-items:center;padding:0 72px;gap:0}
.brand{display:flex;align-items:center;gap:10px;font-size:30px;font-weight:600;color:var(--teal);width:300px}
.brand-dot{width:26px;height:26px;border-radius:50%;background:var(--teal)}
.main-nav{display:flex;gap:21px;font-size:14px;color:#444;margin-left:auto;align-items:center}
.main-nav .active{color:var(--teal)}
.main-nav .phone{color:var(--red);font-weight:600;font-size:15px;margin-left:10px}
.main-nav .login{color:var(--teal);display:flex;align-items:center;gap:6px;margin-left:10px}

/* hero */
.hero{height:553px;position:relative;background:linear-gradient(120deg,#5f9a9a 0%,#8fbdbd 35%,#4b7d86 65%,#b9cfd3 100%)}
.play{position:absolute;width:96px;height:96px;border-radius:50%;background:rgba(255,255,255,.55);display:flex;align-items:center;justify-content:center}
.hero .play{left:552px;top:316px}

/* about */
.about{height:428px;padding-top:68px}
.about h2{margin-bottom:22px}
.about .lead{width:760px;margin:0 auto 20px}
.btn-red{display:block;width:192px;height:36px;line-height:36px;margin:22px auto 0;background:var(--red);color:var(--white);text-align:center;font-size:13px;border-radius:2px}

/* platform */
.platform{height:358px;display:flex}
.platform-text{width:597px;background:var(--teal);color:var(--white);padding:62px 44px 0 73px}
.platform-text h2{text-align:left;color:var(--white);font-size:24px;margin-bottom:14px}
.platform-text p{font-size:14.5px;line-height:1.78}
.platform-media{flex:1;position:relative;background:linear-gradient(110deg,#6f8f95 0%,#a8b9c4 40%,#5e8c8f 70%,#8aa7ae 100%)}
.platform-media .play{left:264px;top:132px}

/* benefits */
.benefits{height:385px;padding-top:68px}
.benefits .lead{width:760px;margin:20px auto 38px}
.benefit-list{display:flex;gap:36px;padding:0 73px}
.benefit{flex:1;display:flex;gap:22px}
.benefit svg{flex:none}
.benefit h3{font-size:16px;font-weight:600;color:var(--ink);margin-bottom:6px}
.benefit p{font-size:12.5px;line-height:1.6;color:var(--muted)}

/* products */
.products{height:623px;background:var(--grey-bg);padding-top:70px}
.products .lead,.solutions .lead{width:760px;margin:18px auto 0}
.product-grid{display:flex;margin:48px 73px 0;background:var(--white)}
.product{width:263.5px;border-right:1px solid #eee}
.product:last-child{border-right:0}
.product-photo{height:205px;background:linear-gradient(160deg,#c6ccd2 0%,#8797a8 45%,#5a7586 75%,#a7b3bd 100%)}
.product-body{padding:22px 20px 26px 20px}
.product h3{font-size:16px;font-weight:600;color:var(--ink);margin-bottom:8px}
.product p{font-size:12.5px;line-height:1.6;color:var(--muted);margin-bottom:10px}
.more{font-size:12.5px;color:var(--red)}
.more::before{content:"•";margin-right:5px}

/* solutions */
.solutions{height:497px;padding-top:56px}
.solution-grid{display:flex;gap:26px;margin:60px 73px 0}
.solution{width:334px;height:239px;display:flex}
.solution-photo{width:167px;background:linear-gradient(150deg,#7d8a94 0%,#3e4d58 50%,#9aa6ae 100%)}
.solution-photo.surgeons{background:linear-gradient(150deg,#8fb4b6 0%,#5d8a8f 50%,#b7c7cb 100%)}
.solution-photo.conference{background:linear-gradient(150deg,#6a6e74 0%,#2e3238 55%,#4a4f55 100%)}
.solution-card{flex:1;background:var(--red);color:var(--white);display:flex;flex-direction:column;align-items:center;padding-top:58px;text-align:center;font-size:14px;line-height:1.45}
.solution-card svg{margin-bottom:12px}
.plus{margin-top:auto;margin-bottom:26px;width:28px;height:28px;border:1px solid rgba(255,255,255,.7);display:flex;align-items:center;justify-content:center;font-size:20px}

/* footer */
.site-footer{height:387px;background:var(--footer-bg);padding:34px 73px 0}
.footer-top{display:flex;align-items:center;height:60px}
.footer-mark{width:54px;height:54px;border-radius:50%;background:var(--teal)}
.footer-nav{display:flex;gap:20px;margin-left:40px;font-size:13px;color:#555}
.social{margin-left:auto;display:flex;gap:8px}
.social span{width:34px;height:34px;border-radius:50%;border:2px solid #b5b5b5}
.footer-cols{display:flex;margin-top:22px}
.footer-col h4{font-size:14px;font-weight:600;color:var(--ink);margin-bottom:10px}
.footer-col{font-size:13px;line-height:1.7;color:#555}
.col-news{width:360px}
.col-contact{width:288px}
.col-products{width:188px}
.field{width:290px;border-bottom:1px solid #999;padding:4px 0 6px;margin-bottom:14px;font-size:13px}
.btn-outline{display:inline-block;border:1px solid #666;padding:2px 10px;font-size:13px;margin-top:2px}
.footer-bottom{display:flex;justify-content:space-between;font-size:12.5px;color:#555;margin-top:78px}
.footer-bottom nav{display:flex;gap:10px}
</style>
</head>
<body>

<header class="site-header">
  <div class="brand"><span class="brand-dot"></span>Plovanta</div>
  <nav class="main-nav">
    <a class="active" href="#">Home</a><a href="#">About</a><a href="#">Features</a><a href="#">Benefits</a><a href="#">Products</a><a href="#">Solutions</a><a href="#">Contact</a>
    <a class="phone" href="#">1800 555 0142</a>
    <a class="login" href="#"><svg width="16" height="16" viewBox="0 0 16 16" fill="none" stroke="currentColor" stroke-width="1.3"><circle cx="8" cy="5" r="3"/><path d="M2 15c0-3.5 2.7-5.5 6-5.5s6 2 6 5.5"/></svg>Login or Sign Up</a>
  </nav>
</header>

<section class="hero" role="img" aria-label="Surgical team in green scrubs operating in a theatre with monitors, video player">
  <span class="play"><svg width="34" height="38" viewBox="0 0 34 38"><path d="M4 2l28 17L4 36z" fill="var(--teal)"/></svg></span>
</section>

<section class="about">
  <h2>About Deferred Live Medical Teaching</h2>
  <p class="lead">Plovanta is building a video based cloud teaching platform for all kinds of medical procedures using synchronized high resolution 360° and wide angle videos in a virtual reality environment. Plovanta changes the way medical procedures are taught.</p>
  <p class="lead">Almost daily medical device companies, doctors and surgeons all over the world develop new or breakthrough products, medical and surgical techniques. These techniques save lives or increase the survival rate of some patients.</p>
  <a class="btn-red" href="#">Expore More</a>
</section>

<section class="platform">
  <div class="platform-text">
    <h2>The Teaching Platform</h2>
    <p>Once the surgery is captured all the info can be streamed online with the unique feature that, although the surgery is filmed in advance, the presenter has real-time full control over the imaging he wants to see. Better than in a live surgery! The presenter of the live session can experience each step of the surgery completely in his own way by navigating through the corresponding omnidirectional imagery.</p>
  </div>
  <div class="platform-media" role="img" aria-label="Surgeons in scrubs watching endoscopic monitors during a procedure, video player">
    <span class="play"><svg width="34" height="38" viewBox="0 0 34 38"><path d="M4 2l28 17L4 36z" fill="var(--teal)"/></svg></span>
  </div>
</section>

<section class="benefits">
  <h2>Benefits</h2>
  <p class="lead">Medical and surgical knowledge can be shared in a faster, easier and more cost-effective way than current solutions like movies and pre-edited video.</p>
  <div class="benefit-list">
    <div class="benefit">
      <svg width="48" height="48" viewBox="0 0 48 48" fill="none" stroke="var(--red)" stroke-width="2"><circle cx="24" cy="24" r="15"/><circle cx="24" cy="9" r="4" fill="#fff"/><circle cx="11" cy="32" r="4" fill="#fff"/><circle cx="37" cy="32" r="4" fill="#fff"/></svg>
      <div><h3>Faster Sharing</h3><p>Faster sharing of knowledge and new techniques to surgeons woldwide due to the cloud-based teaching platform</p></div>
    </div>
    <div class="benefit">
      <svg width="48" height="48" viewBox="0 0 48 48" fill="none" stroke="var(--red)" stroke-width="2"><rect x="4" y="8" width="40" height="26" rx="2"/><path d="M18 42h12M24 34v8M24 14v14M24 14c-3-2-7-2-10 0v14c3-2 7-2 10 0 3-2 7-2 10 0V14c-3-2-7-2-10 0"/></svg>
      <div><h3>Easier Learning</h3><p>Easier learning due to advanced video-based interactivity and state of the art medical illustrations clarifying each step of the procedure</p></div>
    </div>
    <div class="benefit">
      <svg width="48" height="48" viewBox="0 0 48 48" fill="none" stroke="var(--red)" stroke-width="2"><circle cx="24" cy="24" r="19"/><path d="M29 16c-1-2-3-3-5-3-3 0-5 2-5 4.5s2 3.5 5 4.5 5 2 5 4.5-2 4.5-5 4.5c-2 0-4-1-5-3M24 10v28"/></svg>
      <div><h3>More Cost-Effective</h3><p>More cost-effective compared to traditional teaching methods</p></div>
    </div>
  </div>
</section>

<section class="products">
  <h2>Products</h2>
  <p class="lead">It is a long established fact that a reader will be distracted by the readable content of a page more-or-less normal distribution of letters when looking at its layout.</p>
  <div class="product-grid">
    <article class="product"><div class="product-photo" role="img" aria-label="Hybrid operating room with imaging equipment"></div><div class="product-body"><h3>Live</h3><p>It is a long established fact that a reader will be distra more-or-less normal distribution of letters when looking at its layout.</p><a class="more" href="#">More Info</a></div></article>
    <article class="product"><div class="product-photo" role="img" aria-label="Hybrid operating room with imaging equipment"></div><div class="product-body"><h3>Qorvex</h3><p>It is a long established fact that a reader will be distra more-or-less normal distribution of letters when looking at its layout.</p><a class="more" href="#">More Info</a></div></article>
    <article class="product"><div class="product-photo" role="img" aria-label="Hybrid operating room with imaging equipment"></div><div class="product-body"><h3>Qorvex Local</h3><p>It is a long established fact that a reader will be distra more-or-less normal distribution of letters when looking at its layout.</p><a class="more" href="#">More Info</a></div></article>
    <article class="product"><div class="product-photo" role="img" aria-label="Hybrid operating room with imaging equipment"></div><div class="product-body"><h3>Qorvex Cloud</h3><p>It is a long established fact that a reader will be distra more-or-less normal distribution of letters when looking at its layout.</p><a class="more" href="#">More Info</a></div></article>
  </div>
</section>

<section class="solutions">
  <h2>Solutions</h2>
  <p class="lead">It is a long established fact that a reader will be distracted by the readable content of a page more-or-less normal distribution of letters when looking at its layout.</p>
  <div class="solution-grid">
    <div class="solution">
      <div class="solution-photo" role="img" aria-label="Video recording equipment and monitors on a cart"></div>
      <a class="solution-card" href="#">
        <svg width="34" height="34" viewBox="0 0 34 34" fill="none" stroke="#fff" stroke-width="2"><path d="M7 3v9a6 6 0 0 0 12 0V3M13 18v5a7 7 0 0 0 14 0v-4"/><circle cx="27" cy="16" r="3"/></svg>
        For Medical<br>Device Companies<span class="plus">+</span>
      </a>
    </div>
    <div class="solution">
      <div class="solution-photo surgeons" role="img" aria-label="Surgeons in scrubs working in an operating room"></div>
      <a class="solution-card" href="#">
        <svg width="34" height="34" viewBox="0 0 34 34" fill="none" stroke="#fff" stroke-width="2"><path d="M9 10c0-5 3.5-7 8-7s8 2 8 7z"/><path d="M10 12h14v3a7 7 0 0 1-14 0z"/><path d="M4 32c0-6 5-9 13-9s13 3 13 9"/></svg>
        Doctor and<br>Surgeons<span class="plus">+</span>
      </a>
    </div>
    <div class="solution">
      <div class="solution-photo conference" role="img" aria-label="Audience at a medical conference facing a projection screen"></div>
      <a class="solution-card" href="#">
        <svg width="34" height="34" viewBox="0 0 34 34" fill="none" stroke="#fff" stroke-width="2"><rect x="5" y="3" width="24" height="15"/><circle cx="8" cy="24" r="2.5"/><circle cx="17" cy="24" r="2.5"/><circle cx="26" cy="24" r="2.5"/><path d="M3 32c0-3 2-4 5-4s5 1 5 4M12 32c0-3 2-4 5-4s5 1 5 4M21 32c0-3 2-4 5-4s5 1 5 4"/></svg>
        Medical<br>Conferences<span class="plus">+</span>
      </a>
    </div>
  </div>
</section>

<footer class="site-footer">
  <div class="footer-top">
    <span class="footer-mark"></span>
    <nav class="footer-nav"><a href="#">Home</a><a href="#">About</a><a href="#">Features</a><a href="#">Benefits</a><a href="#">Products</a><a href="#">Solutions</a><a href="#">Contact</a></nav>
    <div class="social"><span></span><span></span><span></span><span></span><span></span></div>
  </div>
  <div class="footer-cols">
    <div class="footer-col col-news">
      <h4>Newsletter Sign Up</h4>
      <div class="field">Name</div>
      <div class="field">Email</div>
      <span class="btn-outline">SUBMIT</span>
    </div>
    <div class="footer-col col-contact">
      <h4>Contact Us</h4>
      <p>plovanta deferred live medical teaching<br>14, Carrow Lane, Weston Park,<br>Meridale - 40218</p>
      <p style="margin-top:14px">T: 1800 555 0142<br>E: info@plovanta.example</p>
    </div>
    <div class="footer-col col-products">
      <h4>Our Products</h4>
      <p>Live<br>Qorvex<br>Qorvex Local<br>Qorvex Cloud</p>
    </div>
    <div class="footer-col">
      <h4>Solutions</h4>
      <p>For medical device companies<br>Doctor and surgeons<br>Medical conferences</p>
    </div>
  </div>
  <div class="footer-bottom">
    <span>Copyright 2017 All Rights Reserved.</span>
    <nav><a href="#">Terms of Use</a><a href="#">Privacy Policy</a></nav>
  </div>
</footer>

</body>
</html>
```